Innovative Fashion Business needs Branding and Business Card.

We need a Business Card and Branding work (Email Footer, Stickers, letterhead, all from same Design) We are an innovative, progressive and exciting Fashion Start-up. We are called "Quil Amber" I am attaching the original artwork of the image I want to use. Also have a previous Card, I want to do something like that, only using this new image.

```html
<!DOCTYPE html>
<html lang="en">
<head>
<meta charset="utf-8">
<title>Quil Amber — Business Card</title>
<link href="https://fonts.googleapis.com/css2?family=Montserrat:wght@500;600&family=Roboto+Slab:wght@300&display=swap" rel="stylesheet">
<style>
  :root {
    --stage: #808080;
    --card: #f6f6f4;
    --card-edge: #d8d8d8;
    --purple: #6e4289;
    --purple-light: #b9a0cc;
    --ink: #3a3a3a;
    --ink-soft: #555555;
    --white: #ffffff;
  }
  * { margin: 0; padding: 0; box-sizing: border-box; }
  html, body { width: 1200px; height: 459px; overflow: hidden; background: var(--stage); }
  .stage { position: relative; width: 1200px; height: 459px; }
  .card {
    position: absolute; top: 102px; width: 419px; height: 253px;
    background: var(--card); border: 1px solid var(--card-edge);
    font-family: "Roboto Slab", Georgia, serif; font-weight: 300; color: var(--ink);
  }
  .card--front { left: 158px; }
  .card--back { left: 622px; }

  .wordmark {
    position: absolute; top: 23px; left: 0; width: 100%; text-align: center;
    font-family: "Montserrat", Arial, sans-serif; font-weight: 500;
    font-size: 31px; letter-spacing: 0.5px; color: var(--purple); line-height: 1;
  }
  .artwork {
    position: absolute; left: 106px; top: 60px; width: 208px; height: 156px;
    background: linear-gradient(135deg, #ecebee 0%, #ddd3e4 55%, #c9b6d6 100%);
  }
  .tagline {
    position: absolute; top: 226px; left: 0; width: 100%; text-align: center;
    font-size: 11px; color: var(--ink-soft);
  }

  .person { position: absolute; top: 38px; left: 0; width: 100%; text-align: center; }
  .person__name {
    font-family: "Montserrat", Arial, sans-serif; font-weight: 600;
    font-size: 15px; color: var(--purple); line-height: 1.2;
  }
  .person__role { font-size: 10px; color: var(--ink-soft); margin-top: 2px; }
  .flourish {
    position: absolute; top: 28px; width: 24px; height: 48px;
    background: linear-gradient(180deg, #c2aed2, #8d6aa6);
    border-radius: 12px; opacity: 0.55;
  }
  .flourish--left { left: 102px; }
  .flourish--right { right: 104px; }

  .contact {
    position: absolute; top: 113px; left: 0; width: 100%; text-align: center;
    font-size: 12.5px; line-height: 17px; color: var(--ink); list-style: none;
  }
  .services {
    position: absolute; top: 192px; left: 0; width: 100%; height: 47px;
    background: linear-gradient(90deg, var(--purple) 0%, var(--purple) 55%, var(--purple-light) 100%);
    color: var(--white); text-align: center; font-size: 11.5px; line-height: 15px;
    padding-top: 8px;
  }
</style>
</head>
<body>
<main class="stage">
  <section class="card card--front">
    <h1 class="wordmark">QUIL AMBER</h1>
    <div class="artwork" role="img" aria-label="Line illustration of a couple and a cat with purple hearts and flowers"></div>
    <p class="tagline">Purveyors of Inspiration &amp; Opportunity</p>
  </section>

  <section class="card card--back">
    <div class="flourish flourish--left" role="img" aria-label="Small purple hearts and stars"></div>
    <div class="flourish flourish--right" role="img" aria-label="Small purple hearts and stars"></div>
    <div class="person">
      <h2 class="person__name">Hero Love</h2>
      <p class="person__role">Partner &amp; Strategist</p>
    </div>
    <ul class="contact">
      <li>+852 5550 1846</li>
      <li>hero@quilamber.asia</li>
      <li>www.quilamber.asia</li>
    </ul>
    <div class="services">
      <p>Boutique development &amp; sourcing</p>
      <p>Sustainbility &amp; innovation</p>
    </div>
  </section>
</main>
</body>
</html>
```